Bringing Radiant Artistry and Venturing Expressive Routines

FLYER FOR MENTAL SKILLS TRAINING AND CHOREOGRAPHY
For more information please see attachment.
For more information please see attachment
Thank you..

Target Market(s)

athletes, dancers and choreographers

Industry/Entity Type

Training

Font styles to use
Serif

Colors
32a5d7
0392cd
85cae6

Requirements
Must have
• email address: braverbymarisolquentin@postnest.example
• phone number: (555) 214-7730
• Facebook: www.fanpagehub.example/movementbymarisolquentin
Nice to have
• Everything that is in the file I have attached. Flattering and eye catching unisex color. Logo should be included on the very first page.

```html
<!DOCTYPE html>
<html lang="en">
<head>
<meta charset="utf-8">
<title>BRAVER – Choreography &amp; Mental Skills Flyer</title>
<link href="https://fonts.googleapis.com/css2?family=Source+Sans+3:wght@400;600;700&display=swap" rel="stylesheet">
<style>
  :root{
    --sky:#85cae6;
    --sky-mid:#32a5d7;
    --ocean:#0392cd;
    --ink:#1f1f1f;
    --label-grey:#8a8a8a;
    --frame-grey:#a9a9a9;
    --heading-blue:#1a8fd0;
    --navy:#263d8f;
    --teal:#22b5a0;
    --gold:#f0b030;
    --red:#b0202a;
    --green:#3aaa48;
    --amber:#e08a1e;
    --silhouette:#151515;
  }
  *{box-sizing:border-box;margin:0;padding:0}
  html,body{width:1200px;height:1000px;overflow:hidden;background:#fff}
  body{position:relative;font-family:"Source Sans 3",sans-serif;color:var(--ink)}
  .side-label{position:absolute;top:20px;left:0;width:1200px;text-align:center;font-size:40px;font-weight:700;color:var(--label-grey);letter-spacing:2px}
  .flyer{position:absolute;left:27px;top:78px;width:1143px;height:808px;border:2px solid var(--frame-grey);overflow:hidden;background:#fff}
  .flyer > *{position:absolute}
  .backdrop{left:0;top:0;width:1143px;height:808px}
  .fold-line{left:569px;top:0;height:808px;border-left:2px dashed #c4c4c4}

  /* inside panel */
  .info-panel{left:39px;top:39px;width:494px;height:730px;border:2.5px solid var(--ocean);border-radius:12px;background:rgba(255,255,255,.82)}
  .service{position:absolute;left:62px;width:380px}
  .service .arrow{position:absolute;left:-36px;top:2px}
  .service h3{font-size:17px;font-weight:700;color:var(--heading-blue);line-height:21px}
  .service p{font-size:16px;line-height:21px}
  .packages-tab{position:absolute;left:0;top:245px;width:158px;height:31px;background:var(--navy);color:#fff;font-size:19px;font-weight:700;line-height:31px;padding-left:44px}
  .price-table{position:absolute;left:61px;top:292px;width:404px;border-collapse:collapse;font-size:16px}
  .price-table th{text-align:left;font-weight:700;padding:0 0 2px 30px;height:24px}
  .price-table th:last-child,.price-table td:last-child{padding-left:30px}
  .price-table td{padding:0 0 0 30px;line-height:21px;border-top:2px solid var(--gold)}
  .price-table td:first-child{border-right:2px solid var(--gold);width:190px}
  .price-table tr:last-child td{border-bottom:2px solid var(--gold)}
  .contact-box{position:absolute;left:29px;top:578px;width:435px;height:99px;border:2px solid var(--teal);padding:20px 0 0 20px;font-size:15px;line-height:21.5px}
  .contact-tab{position:absolute;left:167px;top:556px;width:157px;height:30px;background:var(--teal);color:#fff;font-size:19px;font-weight:700;text-align:center;line-height:30px}
  .contact-line{display:flex;align-items:center;gap:7px}
  .contact-line svg{flex:none}

  /* cover */
  .performer-art{width:158px;height:318px;top:36px;background:linear-gradient(180deg,#2a2a2a,var(--silhouette));border-radius:70px 70px 20px 20px;opacity:.95}
  .performer-left{left:695px}
  .performer-right{left:882px}
  .stacked-title{left:838px;top:88px;width:40px;text-align:center;font-size:38px;font-weight:700;line-height:43px;text-shadow:1px 2px 3px rgba(0,0,0,.45)}
  .motto{left:630px;top:368px;width:480px}
  .motto-row{position:absolute;left:0;height:68px;display:flex;align-items:center}
  .motto-badge{width:72px;height:72px;border-radius:50%;display:flex;align-items:center;justify-content:center;opacity:1}
  .motto-badge span{width:52px;height:52px;border-radius:50%;display:flex;align-items:center;justify-content:center;color:#fff;font-size:36px;font-weight:700;border:2px solid rgba(255,255,255,.7)}
  .motto-word{margin-left:6px;font-size:31px;font-weight:700;padding-bottom:2px;border-bottom:2px solid currentColor;padding-right:6px}
  .c-red{color:var(--red)} .bg-red{background:rgba(176,32,42,.45)} .bg-red span{background:var(--red)}
  .c-blue{color:var(--heading-blue)} .bg-blue{background:rgba(26,143,208,.45)} .bg-blue span{background:var(--heading-blue)}
  .c-teal{color:var(--teal)} .bg-teal{background:rgba(34,181,160,.45)} .bg-teal span{background:var(--teal)}
  .c-navy{color:var(--navy)} .bg-navy{background:rgba(38,61,143,.5)} .bg-navy span{background:var(--navy)}
  .c-green{color:var(--green)} .bg-green{background:rgba(58,170,72,.45)} .bg-green span{background:var(--green)}
  .c-amber{color:var(--amber)} .bg-amber{background:rgba(224,138,30,.45)} .bg-amber span{background:var(--amber)}
</style>
</head>
<body>
  <div class="side-label">FRONT</div>

  <main class="flyer">
    <svg class="backdrop" viewBox="0 0 1143 808" aria-hidden="true">
      <defs>
        <linearGradient id="skyFill" x1="0" y1="0" x2="1" y2="1">
          <stop offset="0" stop-color="#9fd6ee"/>
          <stop offset=".55" stop-color="var(--sky)"/>
          <stop offset="1" stop-color="#5dbbe3"/>
        </linearGradient>
      </defs>
      <path d="M0 0H1143V312C1040 350 900 360 760 345C680 336 610 325 570 322C470 322 200 330 0 338Z" fill="url(#skyFill)"/>
      <path d="M0 308C200 320 420 322 570 320C650 330 760 345 880 350C980 352 1070 335 1143 305V330C1060 355 980 366 880 365C760 362 650 346 570 332C420 336 200 350 0 362Z" fill="var(--ocean)"/>
      <path d="M0 330C220 336 430 334 570 322C430 340 220 350 0 362Z" fill="var(--sky-mid)" opacity=".6"/>
    </svg>
    <div class="fold-line"></div>

    <section class="info-panel">
      <div class="service" style="top:39px">
        <svg class="arrow" width="16" height="14" viewBox="0 0 16 14" aria-hidden="true"><circle cx="7" cy="7" r="6" fill="none" stroke="var(--ocean)" stroke-width="2"/><path d="M3 7H13M10 4L13 7L10 10" fill="none" stroke="var(--ocean)" stroke-width="2"/></svg>
        <h3>Individual Sessions</h3>
        <p>Individual sessions are developed specifically for anathlete’s particular needs.</p>
      </div>
      <div class="service" style="top:123px">
        <svg class="arrow" width="16" height="14" viewBox="0 0 16 14" aria-hidden="true"><circle cx="7" cy="7" r="6" fill="none" stroke="var(--ocean)" stroke-width="2"/><path d="M3 7H13M10 4L13 7L10 10" fill="none" stroke="var(--ocean)" stroke-width="2"/></svg>
        <h3>Choreography</h3>
        <p>Choreography can stand alone or be implemented into individual sessions. Dance lessons can also be incorporated into choreography sessions.</p>
      </div>

      <div class="packages-tab">Packages</div>
      <table class="price-table">
        <tr><th>Service</th><th>Price</th></tr>
        <tr><td>Team Workshops</td><td>$250 per contact/hour</td></tr>
        <tr><td>Coach Workshops</td><td>$250 per contact hour</td></tr>
        <tr><td>Individual Sessions</td><td>$100 per contact hour</td></tr>
        <tr><td>Floor Routines<br>Beam Routines</td><td>$400 per gymnast<br>$150 per gymnast</td></tr>
        <tr><td>Dance Lessons</td><td>$25 per contact hour</td></tr>
      </table>

      <div class="contact-box">
        <div class="contact-line"><svg width="13" height="13" viewBox="0 0 13 13" aria-hidden="true"><circle cx="6.5" cy="6.5" r="5" fill="none" stroke="#777" stroke-width="1.5"/><circle cx="6.5" cy="6.5" r="2" fill="none" stroke="#777" stroke-width="1.5"/></svg>Email: braverbymarisolquentin@postnest.example</div>
        <div class="contact-line"><svg width="14" height="13" viewBox="0 0 14 13" aria-hidden="true"><path d="M1 5C1 2 13 2 13 5L11 6L10 4H4L3 6Z M3 7H11L12 12H2Z" fill="#777"/></svg>Ph: (555) 214-7730</div>
        <div class="contact-line"><svg width="13" height="13" viewBox="0 0 13 13" aria-hidden="true"><rect width="13" height="13" fill="var(--navy)"/></svg>www.fanpagehub.example/movementbymarisolquentin</div>
      </div>
      <div class="contact-tab">Contact</div>
    </section>

    <div class="performer-art performer-left" role="img" aria-label="Dark silhouette of a dancer posing with one arm outstretched"></div>
    <div class="performer-art performer-right" role="img" aria-label="Mirrored dark silhouette of a dancer posing with one arm outstretched"></div>

    <div class="stacked-title">
      <div class="c-red">B</div><div class="c-blue">R</div><div class="c-teal">A</div><div class="c-navy">V</div><div class="c-green">E</div><div class="c-amber">R</div>
    </div>

    <section class="motto">
      <div class="motto-row" style="top:0"><div class="motto-badge bg-red"><span>B</span></div><div class="motto-word c-red">ringing</div></div>
      <div class="motto-row" style="top:68px"><div class="motto-badge bg-blue"><span>R</span></div><div class="motto-word c-blue">adiant</div></div>
      <div class="motto-row" style="top:136px"><div class="motto-badge bg-teal"><span>A</span></div><div class="motto-word c-teal">rtistry &amp;</div></div>
      <div class="motto-row" style="top:204px"><div class="motto-badge bg-navy"><span>V</span></div><div class="motto-word c-navy">enturing</div></div>
      <div class="motto-row" style="top:272px"><div class="motto-badge bg-green"><span>E</span></div><div class="motto-word c-green">xpressive</div></div>
      <div class="motto-row" style="top:340px"><div class="motto-badge bg-amber"><span>R</span></div><div class="motto-word c-amber">outines</div></div>
    </section>
  </main>
</body>
</html>
```